Banner to Drive Business Users to Sign Up

Hi,

Banner One (static banner)
I would like you to redesign this page with a single banner of dimensions 600X400:

http://www.tornlark.com.au/Business-Listing.html

The text in the banner should be something like:

Have a Local Business? Advertise directly to people in Your Suburb
List a Local Business, attract Local Customers
List Today and Get a Free Business Page
Upload Pictures To Promote Your Business
Maintain a Blog to Promote Your Business

Of course modifications on this text is allowed.

The site is an Australian site, listing local news and stories from around Australia. The site is broken down into individual suburbs that allow business user to list there business. This allows business to target a specific audience within their local area. Access to screenshots and other images can be provided upon request.
The aim is to create a professional banner that encourages people to sign up. Currently the service is free for 2 months and then $22/year. Any other questions can be answered.

The current page describes the service but is poorly designed.
Banner 2 (static Banner)
If you go to this page:

http://www.tornlark.com.au/

The banner on the right "List your business" needs to be redesigned to complement Banner 1 (can just be scaled down) as above and should draw business users to sign up. Dimensions should be 468 X 60 (which I know is bigger then current banner).

Looking forward to Your Designs

Target Market(s)

Small Business Owners, Australians

Industry/Entity Type

Business

Requirements
Should not have
• Tackiness, or poor graphics

```html
<!DOCTYPE html>
<html lang="en">
<head>
<meta charset="utf-8">
<title>Local Business Listing Banner</title>
<link rel="stylesheet" href="https://fonts.googleapis.com/css2?family=Arimo:wght@700&family=Archivo+Narrow:ital,wght@1,400&display=swap">
<style>
  :root {
    --bg-top: #e4e4e4;
    --bg-bottom: #f1f1f1;
    --swoosh: #fbfbfb;
    --swoosh-edge: #ececec;
    --ink: #111111;
    --ink-soft: #2a2a2a;
    --btn-light: #ffc53a;
    --btn-mid: #ff9c12;
    --btn-dark: #f07800;
    --btn-edge: #d96a00;
    --btn-text: #ffffff;
    --icon-people: #4a4a4a;
    --icon-doc: #efe6cf;
    --icon-window: #4d4d4d;
    --icon-camera: #2f4f9a;
    --icon-bubble: #7a3a9a;
  }
  * { margin: 0; padding: 0; box-sizing: border-box; }
  html, body { width: 1200px; height: 800px; overflow: hidden; }
  body { background: #ffffff; }
  .banner {
    position: relative;
    width: 1200px;
    height: 800px;
    overflow: hidden;
    background: linear-gradient(180deg, var(--bg-top) 0%, var(--bg-bottom) 100%);
    font-family: "Arimo", Arial, sans-serif;
    color: var(--ink);
  }
  .banner__swoosh { position: absolute; left: 0; top: 0; width: 1200px; height: 800px; }
  .banner__headline {
    position: absolute;
    top: 20px;
    left: 0;
    width: 1200px;
    text-align: center;
    font-size: 58px;
    font-weight: 700;
    letter-spacing: 3.5px;
    line-height: 1.2;
    white-space: nowrap;
  }
  .benefits { position: absolute; left: 96px; top: 104px; list-style: none; }
  .benefit {
    position: relative;
    height: 90px;
    display: flex;
    align-items: center;
    padding-left: 116px;
    font-size: 35px;
    font-weight: 700;
    letter-spacing: 1.7px;
    white-space: nowrap;
  }
  .benefit__icon { position: absolute; left: 0; top: 50%; transform: translateY(-50%); }
  .benefit__icon--people { width: 84px; height: 70px; border-radius: 40px 40px 10px 10px; background: radial-gradient(circle at 50% 30%, #6a6a6a, var(--icon-people)); }
  .benefit__icon--doc { width: 70px; height: 74px; border-radius: 6px; background: linear-gradient(180deg, #f8f2e2, var(--icon-doc)); border: 2px solid #c9bfa5; }
  .benefit__icon--window { width: 86px; height: 64px; border-radius: 6px; background: linear-gradient(180deg, #6a6a6a, var(--icon-window)); border: 2px solid #9a9a9a; }
  .benefit__icon--camera { width: 88px; height: 62px; border-radius: 8px; background: radial-gradient(circle at 50% 55%, #6b8fd6, var(--icon-camera)); }
  .benefit__icon--bubble { width: 84px; height: 62px; border-radius: 50%; background: radial-gradient(circle at 45% 35%, #b075cf, var(--icon-bubble)); }
  .signup {
    position: absolute;
    left: 362px;
    top: 600px;
    width: 442px;
    height: 104px;
    border-radius: 10px;
    border: 3px solid var(--btn-edge);
    background: linear-gradient(180deg, var(--btn-light) 0%, var(--btn-mid) 48%, var(--btn-dark) 100%);
    box-shadow: 0 6px 10px rgba(0,0,0,0.22), inset 0 2px 0 rgba(255,255,255,0.55);
    display: flex;
    align-items: center;
    justify-content: center;
    color: var(--btn-text);
    font-size: 42px;
    font-weight: 700;
    letter-spacing: 1px;
    text-decoration: none;
    text-shadow: 0 2px 2px rgba(120,50,0,0.45);
  }
  .offer {
    position: absolute;
    top: 726px;
    left: 0;
    width: 1200px;
    text-align: center;
    font-family: "Archivo Narrow", "Arial Narrow", sans-serif;
    font-style: italic;
    font-weight: 400;
    font-size: 48px;
    color: var(--ink-soft);
    word-spacing: 4px;
    white-space: nowrap;
  }
</style>
</head>
<body>
  <div class="banner">
    <svg class="banner__swoosh" viewBox="0 0 1200 800" aria-hidden="true">
      <path d="M0 600 C 300 520, 700 500, 1200 560 L1200 800 L0 800 Z" fill="var(--swoosh)"/>
      <path d="M0 560 C 350 480, 800 470, 1200 520 L1200 560 C 700 500, 300 520, 0 600 Z" fill="var(--swoosh-edge)"/>
    </svg>

    <h1 class="banner__headline">DO YOU HAVE A LOCAL BUSINESS?</h1>

    <ul class="benefits">
      <li class="benefit"><span class="benefit__icon benefit__icon--people" role="img" aria-label="Icon of a group of people"></span>Advertise directly to people in Your Suburb</li>
      <li class="benefit"><span class="benefit__icon benefit__icon--doc" role="img" aria-label="Icon of a listing document"></span>List a Local Business, attract Local Customers</li>
      <li class="benefit"><span class="benefit__icon benefit__icon--window" role="img" aria-label="Icon of a web page window"></span>List Today and Get a Free Business Page</li>
      <li class="benefit"><span class="benefit__icon benefit__icon--camera" role="img" aria-label="Icon of a camera"></span>Upload Pictures To Promote Your Business</li>
      <li class="benefit"><span class="benefit__icon benefit__icon--bubble" role="img" aria-label="Icon of a speech bubble"></span>Maintain a Blog to Promote Your Business</li>
    </ul>

    <a class="signup" href="#signup">SIGN UP NOW</a>

    <p class="offer">Current Special&nbsp; 2&nbsp; months Free Listing</p>
  </div>
</body>
</html>
```